Business Card for boutique psychology business

Business card for boutique psychology practice in Melbourne. I want them to be relatively simply with the logo and backing colour taking up the front side. Then, text on the back, with my name; professional title (Clinical Psychologist); website - torvinpsychology.com.au; email: hello@torvinpsychology.com.au; insta: @torvin.psychology.emdr
Back should also have the words: Connect. Integrate. Evolve
Fonts used for logo are: Mikea Demo and Gotham Medium. Use something for back text that will compliment these.
Brand colours uploaded below. I'd like to see options in both olive and blush.

```html
<!DOCTYPE html>
<html lang="en">
<head>
<meta charset="utf-8">
<title>Torvin Psychology – Business Cards</title>
<link rel="stylesheet" href="https://fonts.googleapis.com/css2?family=Josefin+Sans:wght@300;400&family=Montserrat:wght@500&display=swap">
<style>
  :root {
    --backdrop: #141414;
    --paper: #ffffff;
    --olive: #434530;
    --olive-ink: #3d3f2a;
    --blush: #e8cdbb;
  }
  * { margin: 0; padding: 0; box-sizing: border-box; }
  html, body { width: 1189px; height: 1200px; overflow: hidden; background: var(--backdrop); }
  .canvas { position: relative; width: 1189px; height: 1200px; }

  .card { position: absolute; }
  .card--front { left: 169px; top: 111px; width: 851px; height: 486px; background: var(--paper); color: var(--olive-ink); }
  .card--back { left: 168px; top: 640px; width: 854px; height: 488px; background: var(--olive); color: var(--blush); }

  .brand-name {
    position: absolute;
    font-family: "Josefin Sans", sans-serif;
    font-weight: 300;
    line-height: 1;
    letter-spacing: -0.01em;
    white-space: nowrap;
  }
  .brand-sub {
    position: absolute;
    font-family: "Montserrat", sans-serif;
    font-weight: 500;
    line-height: 1;
    letter-spacing: 0.01em;
    white-space: nowrap;
  }

  .card--front .brand-name { left: 0; width: 100%; text-align: center; top: 182px; font-size: 130px; }
  .card--front .brand-sub { left: 0; width: 100%; text-align: center; top: 304px; font-size: 28px; }
  .tagline {
    position: absolute; left: 0; width: 100%; top: 402px; text-align: center;
    font-family: "Josefin Sans", sans-serif; font-weight: 300; font-size: 21px;
    letter-spacing: 0.14em; line-height: 1; white-space: nowrap;
  }
  .tagline .divider { margin: 0 0.7em 0 0.3em; }

  .back-brand { position: absolute; right: 67px; top: 100px; width: 300px; }
  .card--back .brand-name { left: 0; width: 100%; text-align: center; top: 0; font-size: 100px; }
  .card--back .brand-sub { left: 0; width: 100%; text-align: center; top: 97px; font-size: 25px; }

  .person { position: absolute; left: 54px; top: 282px; font-family: "Josefin Sans", sans-serif; font-weight: 300; line-height: 1; }
  .person__name { font-size: 32px; letter-spacing: 0.03em; }
  .person__role { font-size: 21px; margin-top: 6px; letter-spacing: 0.02em; }

  .contact-list { position: absolute; left: 54px; top: 368px; list-style: none; font-family: "Josefin Sans", sans-serif; font-weight: 300; font-size: 20px; line-height: 1; }
  .contact-list li { display: flex; align-items: center; height: 26px; }
  .contact-list svg { width: 16px; height: 16px; margin-right: 13px; flex: none; }
</style>
</head>
<body>
<main class="canvas">

  <section class="card card--front" aria-label="Card front">
    <div class="brand-name">torvin</div>
    <div class="brand-sub">psychology + EMDR</div>
    <p class="tagline">CONNECT<span class="divider">|</span>INTEGRATE<span class="divider">|</span>EVOLVE</p>
  </section>

  <section class="card card--back" aria-label="Card back">
    <div class="back-brand">
      <div class="brand-name">torvin</div>
      <div class="brand-sub">psychology + EMDR</div>
    </div>

    <div class="person">
      <div class="person__name">Daniel&nbsp; Reeve</div>
      <div class="person__role">Clinical Psychologist</div>
    </div>

    <ul class="contact-list">
      <li>
        <svg viewBox="0 0 16 16" aria-hidden="true"><rect x="1" y="3" width="14" height="10" fill="var(--blush)"/><path d="M1 3 L8 9 L15 3" fill="none" stroke="var(--olive)" stroke-width="1.4"/></svg>
        hello@torvinpsychology.com.au
      </li>
      <li>
        <svg viewBox="0 0 16 16" aria-hidden="true"><circle cx="8" cy="8" r="6.5" fill="var(--blush)"/></svg>
        @torvin.psychology.emdr
      </li>
      <li>
        <svg viewBox="0 0 16 16" aria-hidden="true"><g fill="none" stroke="var(--blush)" stroke-width="1.2"><circle cx="8" cy="8" r="6.5"/><ellipse cx="8" cy="8" rx="3" ry="6.5"/><path d="M1.5 8 H14.5 M2.8 4.5 H13.2 M2.8 11.5 H13.2"/></g></svg>
        torvinpsychology.com.au
      </li>
    </ul>
  </section>

</main>
</body>
</html>
```